Helen's 40th Invitation

I need an invitation designed for a 40th birthday in Singapore. The theme is a "long lunch", set in a colonial garden (black and white house - Singapore style if you want to Google or Bing it).
Look and feel should be simple, elegant, stylish, bold, fresh, minimalist. Nothing fussy, intricate, formal or too colourful. No intials, not wedding-like, minimal colour (no golds).
Setting will be garden setting with champagne, white marquee, white table cloths, long trestle tables, fresh white floowers (lilys or hydrangas).
Format should be PC friendly (jpeg, gif, pdf etc).
Size is flexible to accomodate design - it will be emailed as an attachment.
Details to include:
- Saturday, 27th November, 2010
Time - From 1pm.
Address - 215 Thornbury Park, Singapore
Dress: Garden Glam
RSVP - jlowden@tevarondi.com by 13 November, 2010

```html
<!DOCTYPE html>
<html lang="en">
<head>
<meta charset="utf-8">
<title>Helen's 40th Birthday Invitation</title>
<link rel="stylesheet" href="https://fonts.googleapis.com/css2?family=Italianno&family=Lora:ital,wght@1,700&display=swap">
<style>
  :root {
    --paper: #ffffff;
    --pink-deep: #f6aef3;
    --pink-mid: #fcd4fa;
    --orb-top: #d49bb0;
    --orb-mid: #ebc6d4;
    --orb-pale: #fbf0f5;
    --title-pink: #d98ad6;
    --number-pink: #e6a0e2;
    --birthday-grey: #b9a9b9;
    --detail-ink: #5e4a5c;
    --rsvp-ink: #3c3c3c;
    --flower-mauve: #9e8194;
    --flower-teal: #9ccfd0;
    --flower-green: #b4dcae;
  }
  html, body {
    margin: 0;
    padding: 0;
    width: 1200px;
    height: 944px;
    overflow: hidden;
    background: var(--paper);
  }
  .invitation {
    display: block;
    width: 1200px;
    height: 944px;
  }
  .invitation-title {
    font-family: "Italianno", cursive;
    font-size: 150px;
    fill: var(--title-pink);
    opacity: 0.8;
  }
  .age-number {
    font-family: "Italianno", cursive;
    font-size: 185px;
    fill: var(--number-pink);
  }
  .age-word {
    font-family: "Italianno", cursive;
    font-size: 90px;
    fill: none;
    stroke: var(--birthday-grey);
    stroke-width: 1.4;
  }
  .event-detail {
    font-family: "Italianno", cursive;
    font-size: 60px;
    fill: var(--detail-ink);
  }
  .rsvp-line {
    font-family: "Lora", serif;
    font-style: italic;
    font-weight: 700;
    font-size: 30px;
    letter-spacing: 3px;
    fill: var(--rsvp-ink);
  }
</style>
</head>
<body>
<svg class="invitation" viewBox="0 0 1200 944" xmlns="http://www.w3.org/2000/svg">
  <defs>
    <linearGradient id="panel-wash" x1="0" y1="0" x2="1" y2="1">
      <stop offset="0" stop-color="var(--pink-deep)"/>
      <stop offset="0.5" stop-color="var(--pink-mid)"/>
      <stop offset="1" stop-color="var(--paper)"/>
    </linearGradient>
    <linearGradient id="orb-shade" x1="0.15" y1="0.1" x2="0.85" y2="0.95">
      <stop offset="0" stop-color="var(--orb-top)" stop-opacity="0.85"/>
      <stop offset="0.5" stop-color="var(--orb-mid)" stop-opacity="0.7"/>
      <stop offset="1" stop-color="var(--orb-pale)" stop-opacity="0.6"/>
    </linearGradient>
    <radialGradient id="bloom-mauve" cx="0.5" cy="0.5" r="0.5">
      <stop offset="0" stop-color="var(--flower-mauve)" stop-opacity="0.35"/>
      <stop offset="1" stop-color="var(--flower-mauve)" stop-opacity="0"/>
    </radialGradient>
    <radialGradient id="bloom-teal" cx="0.5" cy="0.5" r="0.5">
      <stop offset="0" stop-color="var(--flower-teal)" stop-opacity="0.55"/>
      <stop offset="1" stop-color="var(--flower-teal)" stop-opacity="0"/>
    </radialGradient>
    <radialGradient id="bloom-green" cx="0.5" cy="0.5" r="0.5">
      <stop offset="0" stop-color="var(--flower-green)" stop-opacity="0.55"/>
      <stop offset="1" stop-color="var(--flower-green)" stop-opacity="0"/>
    </radialGradient>
    <filter id="soft-edge" x="-5%" y="-5%" width="110%" height="110%">
      <feGaussianBlur stdDeviation="2"/>
    </filter>
    <filter id="title-glow" x="-10%" y="-30%" width="120%" height="160%">
      <feGaussianBlur in="SourceGraphic" stdDeviation="3" result="blur"/>
      <feMerge><feMergeNode in="blur"/><feMergeNode in="SourceGraphic"/></feMerge>
    </filter>
    <filter id="number-glow" x="-20%" y="-20%" width="140%" height="140%">
      <feGaussianBlur in="SourceAlpha" stdDeviation="5"/>
      <feOffset dx="3" dy="4"/>
      <feComponentTransfer><feFuncA type="linear" slope="0.4"/></feComponentTransfer>
      <feMerge><feMergeNode/><feMergeNode in="SourceGraphic"/></feMerge>
    </filter>
  </defs>

  <rect class="background-panel" x="0" y="0" width="1083" height="900" fill="url(#panel-wash)"/>

  <ellipse class="centre-orb" cx="668" cy="556" rx="408" ry="322" transform="rotate(-8 668 556)" fill="url(#orb-shade)" filter="url(#soft-edge)"/>

  <g class="flower-artwork">
    <ellipse role="img" aria-label="Large outlined five-petal flower in soft mauve" cx="480" cy="620" rx="260" ry="250" fill="url(#bloom-mauve)"/>
    <ellipse role="img" aria-label="Small outlined flower in pale teal" cx="905" cy="375" rx="150" ry="130" fill="url(#bloom-teal)"/>
    <ellipse role="img" aria-label="Looping green leaves and stem" cx="770" cy="640" rx="180" ry="150" fill="url(#bloom-green)"/>
  </g>

  <text class="invitation-title" transform="translate(48 178) rotate(-10)" filter="url(#title-glow)">Invitation</text>

  <text class="age-number" x="862" y="168" filter="url(#number-glow)">40</text>
  <text class="age-word" transform="translate(815 258) rotate(-16)">Birthday</text>

  <g class="event-details" transform="translate(34 452) rotate(-20)">
    <text class="event-detail" x="0" y="0">On: Saturday, 27.November 2010 - from 1.00 pm.</text>
    <text class="event-detail" x="6" y="58">Address: 215 Thornbury Park, Singapore</text>
    <text class="event-detail" x="12" y="116">Dress: Garden Glam</text>
  </g>

  <text class="rsvp-line" x="78" y="928">RSVP - jlowden@tevarondi.com by 13,November 2010</text>
</svg>
</body>
</html>
```